Resume for higher management position in a mechanical/consultant industries application*

I would like to use this resume for getting a higher position interview possibilities. My skills are multi-cultural negotiation, mechanical industry sales, outsourcing to Asia, ability to manage the agent/reseller system, well team player. multi-language Chinese/English/German specialized. Please make the design, professional, comfortable to read atmosphere.

Target Market(s)

management position, sales related

Font styles to use
Serif
Sans Serif

```html
<!DOCTYPE html>
<html lang="en">
<head>
<meta charset="utf-8">
<title>Lin-Wei Hsu – Sales Manager Resume</title>
<link href="https://fonts.googleapis.com/css2?family=Montserrat:wght@400;500;600&family=Roboto:wght@300;400;700&display=swap" rel="stylesheet">
<style>
  :root {
    --ink: #434343;
    --text: #4a4a4a;
    --paper: #ffffff;
    --backdrop: #efeeec;
    --photo: #b9b9b9;
    --dot-off: #c8c8c8;
  }
  html, body {
    margin: 0; padding: 0;
    width: 1200px; height: 1200px;
    overflow: hidden;
    background: var(--backdrop);
  }
  .sheet {
    position: absolute; left: 173px; top: 0;
    width: 1062px; height: 1492px;
    background: var(--paper);
    transform: scale(0.80429);
    transform-origin: 0 0;
    font-family: "Roboto", sans-serif;
    color: var(--text);
    overflow: hidden;
  }
  .abs { position: absolute; margin: 0; white-space: nowrap; }
  .header-shape { position: absolute; left: 0; top: 0; }
  .name {
    left: 370px; top: 140px;
    font-family: "Montserrat", sans-serif; font-weight: 500;
    font-size: 48px; letter-spacing: 3px; color: #fff;
  }
  .role-title {
    left: 370px; top: 200px;
    font-family: "Montserrat", sans-serif; font-weight: 500;
    font-size: 24px; letter-spacing: 2px; color: #fff;
  }
  .social { left: 780px; font-size: 13px; color: #fff; letter-spacing: 1px; width: 92px; text-align: right; }
  .contact { left: 467px; font-size: 15px; letter-spacing: 1.5px; font-weight: 300; color: var(--text); }
  .personal { left: 763px; font-size: 15px; font-weight: 300; color: var(--text); }
  .profile-link {
    left: 740px; top: 404px; width: 322px; height: 45px;
    background: var(--ink); border-radius: 8px;
    color: #fff; font-size: 14px; line-height: 17px;
    text-align: center; padding-top: 5px; box-sizing: border-box;
  }
  .section-bar {
    position: absolute; background: var(--ink); color: #fff;
    font-family: "Montserrat", sans-serif; font-weight: 500;
    font-size: 28px; letter-spacing: 2px; margin: 0;
    display: flex; align-items: center; box-sizing: border-box;
  }
  .section-bar svg { position: absolute; }
  .para {
    left: 27px; font-size: 14.5px; line-height: 17.9px;
    letter-spacing: 1.5px; font-weight: 300; color: var(--text);
  }
  .skill { left: 26px; font-size: 17px; line-height: 21px; letter-spacing: 1.5px; font-weight: 300; color: var(--text); }
  .school { left: 477px; font-size: 19px; letter-spacing: 1.6px; font-weight: 300; color: var(--text); }
  .degree { left: 507px; font-size: 16px; letter-spacing: 1.5px; font-weight: 300; color: var(--text); }
  .years { left: 827px; font-size: 19px; letter-spacing: 1.6px; font-weight: 300; color: var(--text); }
  .divider { display: inline-block; width: 3px; height: 20px; background: var(--ink); vertical-align: middle; margin-right: 8px; }
  .company { left: 476px; font-size: 18px; letter-spacing: 2px; font-weight: 700; color: var(--ink); }
  .position { left: 791px; font-size: 15px; letter-spacing: 1.5px; font-weight: 300; color: var(--text); }
  .position b { display: inline-block; width: 3px; height: 18px; background: var(--ink); vertical-align: middle; margin-right: 19px; }
  .period { left: 476px; font-size: 19px; letter-spacing: 1.6px; font-weight: 300; color: var(--text); }
  .duty { left: 477px; font-size: 14.5px; line-height: 19px; letter-spacing: 1.5px; font-weight: 300; color: var(--text); }
  .lang { left: 80px; font-size: 19px; letter-spacing: 2px; font-weight: 300; color: var(--text); }
  .footer { position: absolute; left: 0; top: 1439px; width: 1062px; height: 53px; background: var(--ink); }
</style>
</head>
<body>
<main class="sheet">

  <svg class="header-shape" width="1062" height="440" viewBox="0 0 1062 440">
    <path d="M0 0 H1062 V292 H470 C420 292 395 315 365 350 C330 392 300 407 250 407 H0 Z" fill="var(--ink)"/>
    <circle cx="190" cy="204" r="138" fill="#fff"/>
    <circle cx="190" cy="204" r="128" fill="var(--ink)"/>
    <circle cx="190" cy="204" r="113" fill="var(--photo)" role="img" aria-label="Portrait photo of the candidate"/>
    <g fill="none" stroke="#fff" stroke-width="3">
      <circle cx="901" cy="94" r="19"/>
      <circle cx="901" cy="157" r="19"/>
      <circle cx="901" cy="220" r="19"/>
    </g>
    <g fill="var(--ink)">
      <circle cx="425" cy="333" r="16"/>
      <circle cx="425" cy="372" r="16"/>
      <circle cx="425" cy="411" r="16"/>
    </g>
    <g fill="none" stroke="#fff" stroke-width="1.6">
      <rect x="417" y="327" width="16" height="12" rx="1"/>
      <path d="M417 328 L425 334 L433 328"/>
      <rect x="420" y="401" width="10" height="19" rx="2"/>
    </g>
    <path d="M425 364 a6 6 0 0 1 6 6 c0 5 -6 11 -6 11 s-6 -6 -6 -11 a6 6 0 0 1 6 -6 z" fill="#fff"/>
    <circle cx="425" cy="370" r="2.3" fill="var(--ink)"/>
  </svg>

  <h1 class="abs name">Lin-Wei Hsu</h1>
  <p class="abs role-title">SALES MANAGER</p>

  <p class="abs social" style="top:86px">Pagely</p>
  <p class="abs social" style="top:149px">Snapline</p>
  <p class="abs social" style="top:212px">Chatterly</p>

  <p class="abs contact" style="top:324px">xxxxx@mailbox.com</p>
  <p class="abs contact" style="top:363px">xxxxxxxx, Germany</p>
  <p class="abs contact" style="top:402px">+ x (xxx) xxxx</p>
  <p class="abs personal" style="top:324px">Date &amp; Place of birth : xxxxxxx</p>
  <p class="abs personal" style="top:363px">Nationality : Taiwanese</p>
  <div class="abs profile-link">For more information, please visit my ProfileNet<br>https://www.profilenet.com/in/xxxx</div>

  <h2 class="section-bar" style="left:0;top:465px;width:398px;height:42px;padding-left:77px">PROFILE
    <svg style="left:348px;top:8px" width="24" height="26" viewBox="0 0 24 26"><circle cx="12" cy="7" r="6" fill="#fff"/><path d="M2 25 C2 17 6 14 12 14 C18 14 22 17 22 25 Z" fill="#fff"/></svg>
  </h2>
  <p class="abs para" style="top:531px">Currently, I am a "Sales manager Asia" of<br>a top German rotary table company. I am<br>in charge of four countries Japan, China,<br>South Korea and Taiwan with 3 agents,<br>more than 20 salemen team.</p>
  <p class="abs para" style="top:638px">As a director of manufacuting, I have<br>more than 5 years professional experi-<br>ences in manufacturing metal components<br>by different CNC-machines. I am capable<br>of coding CNC G,M-code, designing the<br>working path of different parts and man-<br>aging the whole process.I have well-un-<br>derstanding of mechanical outsourcing<br>ecosystem in Taiwan. With deep knowl-<br>edge of outsourcing metal components<br>to different suppliers in Taiwan.</p>
  <p class="abs para" style="top:852px">Familiar with coordinating with different<br>industrial processes in order to build the<br>final products. (Black oxidizing, Different<br>anodizing, Chemical polishing, Manga-<br>nese phosphate coating, Heat treatment,<br>and Different grinding methods) Especial-<br>ly love to build prototype in order to get a<br>high profitable potential products. (from<br>zero to one)</p>

  <h2 class="section-bar" style="left:0;top:1024px;width:398px;height:44px;padding-left:78px">SKILLS
    <svg style="left:347px;top:9px" width="26" height="26" viewBox="0 0 26 26"><g fill="#fff"><circle cx="13" cy="13" r="8.5"/><rect x="10.5" y="1" width="5" height="24" rx="1"/><rect x="10.5" y="1" width="5" height="24" rx="1" transform="rotate(45 13 13)"/><rect x="10.5" y="1" width="5" height="24" rx="1" transform="rotate(90 13 13)"/><rect x="10.5" y="1" width="5" height="24" rx="1" transform="rotate(135 13 13)"/></g><circle cx="13" cy="13" r="3.6" fill="var(--ink)"/></svg>
  </h2>
  <p class="abs skill" style="top:1082px">Great experiences in handling business<br>with Chinese-cultural business firms.</p>
  <p class="abs skill" style="top:1132px">Multi-national corporation skills<br>(especially in Chinese-speakingmarket)</p>
  <p class="abs skill" style="top:1189px">OEM skills</p>
  <span class="abs" style="left:192px;top:1190px;width:3px;height:20px;background:var(--ink)"></span>
  <p class="abs skill" style="left:251px;top:1189px">Trade skills</p>

  <h2 class="section-bar" style="left:0;top:1225px;width:398px;height:44px;padding-left:78px">LANGUAGE
    <svg style="left:347px;top:10px" width="26" height="24" viewBox="0 0 26 24"><path d="M13 1 C20 1 25 5 25 11 C25 17 20 21 13 21 C11 21 9.5 20.7 8 20.2 L2 23 L4 17.5 C2 15.8 1 13.5 1 11 C1 5 6 1 13 1 Z" fill="#fff"/></svg>
  </h2>
  <p class="abs lang" style="top:1294px">Chinese</p>
  <p class="abs lang" style="top:1334px">English</p>
  <p class="abs lang" style="top:1372px">German</p>
  <svg class="abs" style="left:215px;top:1297px" width="120" height="96" viewBox="0 0 120 96" role="img" aria-label="Language levels: Chinese 5 of 5, English 4 of 5, German 4 of 5">
    <g fill="var(--ink)">
      <circle cx="10" cy="10" r="6"/><circle cx="35" cy="10" r="6"/><circle cx="60" cy="10" r="6"/><circle cx="85" cy="10" r="6"/><circle cx="109" cy="10" r="6"/>
      <circle cx="10" cy="50" r="6"/><circle cx="35" cy="50" r="6"/><circle cx="60" cy="50" r="6"/><circle cx="85" cy="50" r="6"/>
      <circle cx="10" cy="88" r="6"/><circle cx="35" cy="88" r="6"/><circle cx="60" cy="88" r="6"/><circle cx="85" cy="88" r="6"/>
    </g>
    <g fill="var(--dot-off)"><circle cx="109" cy="50" r="6"/><circle cx="109" cy="88" r="6"/></g>
  </svg>

  <h2 class="section-bar" style="left:467px;top:465px;width:595px;height:44px;padding-left:39px">EDUCATION
    <svg style="left:365px;top:8px" width="40" height="28" viewBox="0 0 40 28"><path d="M20 2 L38 10 L20 18 L2 10 Z" fill="#fff"/><path d="M9 14 V21 C9 24 14 26 20 26 C26 26 31 24 31 21 V14 L20 19 Z" fill="#fff"/></svg>
  </h2>
  <p class="abs school" style="top:532px">Tai-Ho Technical University</p>
  <p class="abs years" style="top:532px"><span class="divider"></span>2005 - 2009</p>
  <p class="abs degree" style="top:558px">Bachelor of Chemical engineering</p>
  <p class="abs school" style="top:597px">Accademia Tecnica di Milano</p>
  <p class="abs years" style="top:598px"><span class="divider"></span>2011 - 2012</p>
  <p class="abs degree" style="top:623px">Master of Business Administration</p>

  <h2 class="section-bar" style="left:465px;top:675px;width:595px;height:43px;padding-left:39px">EXPERIENCE
    <svg style="left:369px;top:7px" width="32" height="30" viewBox="0 0 32 30"><rect x="1" y="1" width="30" height="20" rx="2" fill="#fff"/><rect x="5" y="5" width="22" height="12" fill="var(--ink)"/><rect x="13" y="21" width="6" height="5" fill="#fff"/><rect x="8" y="26" width="16" height="3" fill="#fff"/></svg>
  </h2>

  <p class="abs company" style="top:742px">Asiaxxxxxxxxx</p>
  <p class="abs position" style="top:744px"><b></b>Sales Manager</p>
  <p class="abs period" style="top:772px">2018 - Now</p>
  <p class="abs duty" style="top:801px">Currently, leading 3 major dealers in Taiwan, Mainland<br>China, South Korea and Japan with more than 20 sales-<br>men team.<br>Kelmarant provides rotary tables, trunnions and 2 axis<br>rotary tilt units shall have the best possible technical<br>characteristics in the smallest possible space, is the<br>principle model for our dividing heads -engineering<br>-manufacturing -and assembly.</p>

  <p class="abs company" style="top:969px">Ostwald Precision Machinery</p>
  <p class="abs position" style="top:970px"><b></b>Director of Manufacturing</p>
  <p class="abs period" style="top:991px">2012 - 2017</p>
  <p class="abs duty" style="top:1018px">Using CNC turn/mill machine to manufacture any mechan-<br>ical components as customers want. Also providing great<br>total solutions for our clients.<br>Photos shown in my profile are my products which are<br>made by CNC turn-milling dual spindles machines(trophy<br>is programmed by CAM).</p>

  <p class="abs company" style="top:1153px">Brightway Import Mannheim</p>
  <p class="abs position" style="top:1154px"><b></b>Marketing Analyst</p>
  <p class="abs period" style="top:1180px">2012 Apr - 2012 Nov</p>
  <p class="abs duty" style="top:1207px">Help Brightway Import to build their sales/marketing<br>strategy for the new launched product "Slick-Guard" in<br>central Europe.</p>

  <p class="abs company" style="top:1285px">Calvessa Group Bergamo</p>
  <p class="abs position" style="top:1286px"><b></b>External consultant</p>
  <p class="abs period" style="top:1312px">2011 Oct - 2012 Mar</p>
  <p class="abs duty" style="top:1339px">To improve the Quenby solution(ERP system) of Calves-<br>sa with re-organized procurement process and new<br>standardized KPIs.</p>

  <div class="footer"></div>
</main>
</body>
</html>
```